PowerPoint Template - Multiple Slide Backgrounds

Looking for a professional PowerPoint template for a technology company. You will see with the logo there's sort of a theme with gears and a lightbulb of sorts. Keeping with this sort of design could help with the brand.

Branding information
• Logo with transparent background included
• Primary Color (Orange) Hex #E6753D
• Secondary Color (Brown) Hex #6A4238
• Primary Font - Myriad Pro
• Secondary Font - Quiet Sans Light

Design request -
• PowerPoint (POTX) template with master slide views
• Cover Slide
• Color Pallet - 7 Color PowerPoint pallet that includes and complements primary and secondary colors
• Slide Master with Footer
• Multiple Background Types to allow for smart art overlay or bullet point text boxes
Bonus - Sample graphical elements using shapes and smart art

```html
<!DOCTYPE html>
<html lang="en">
<head>
<meta charset="utf-8">
<title>Lakeline DevOps – Second Part</title>
<link rel="stylesheet" href="https://fonts.googleapis.com/css2?family=Source+Sans+3:wght@400;600;700&family=Arimo:wght@700&display=swap">
<style>
  :root{
    --brown:#6A4238;
    --orange:#E6753D;
    --peach:#F0A878;
    --navy:#0f3a70;
    --canvas:#ebebeb;
    --slide:#ffffff;
    --footer:#5b5b5b;
    --grid:#e3e3e3;
    --ink:#3a3a3a;
    --muted:#666;
    --row:#f2f2f2;
    --map:#8a8a8a;
    --caption:#12578f;
  }
  *{box-sizing:border-box;margin:0;padding:0}
  html,body{width:1200px;height:1050px;overflow:hidden;background:var(--canvas)}
  body{position:relative;font-family:"Source Sans 3",Arial,sans-serif;color:var(--ink)}
  .slide{position:absolute;width:557px;height:313px;background:var(--slide);overflow:hidden}
  .slide--1{left:21px;top:13px}
  .slide--2{left:618px;top:13px}
  .slide--3{left:21px;top:335px}
  .slide--4{left:618px;top:335px}
  .slide--5{left:21px;top:660px}
  .slide--6{left:618px;top:660px}
  .slide__title{position:absolute;left:18px;top:18px;font-size:21px;font-weight:700;color:var(--brown);letter-spacing:.2px}
  .slide__rule{position:absolute;left:18px;top:51px;width:70px;height:1.5px;background:var(--orange)}
  .brand{position:absolute;right:18px;top:14px;width:60px;text-align:center}
  .brand__dot{display:block;width:14px;height:14px;border-radius:50%;border:2px solid var(--brown);margin:0 auto 2px}
  .brand__name{font-size:6.5px;font-weight:600;color:var(--brown);white-space:nowrap}
  .footer{position:absolute;left:0;right:0;bottom:0;height:18px;background:var(--footer)}
  .footer__label{position:absolute;left:17px;top:5px;font-size:6px;font-weight:600;color:#fff}
  .footer__page{position:absolute;right:0;bottom:0;width:46px;height:24px;background:var(--brown);
    clip-path:polygon(8px 0,100% 0,100% 100%,0 100%);color:#fff;font-size:7px;text-align:center;line-height:24px;padding-left:6px}
  .chart{position:absolute;font-family:"Source Sans 3",Arial,sans-serif}
  .copy{position:absolute;left:18px;width:200px}
  .copy__head{font-size:12.5px;font-weight:700;color:var(--brown);margin-bottom:12px}
  .copy__body{font-size:7.5px;line-height:1.45;color:var(--muted)}
  .divider{position:absolute;width:1px;background:#cfcfcf}
  .photo{position:absolute;left:299px;top:64px;width:241px;height:214px;
    background:linear-gradient(120deg,#f4f1ec 0%,#d9cabb 35%,#7b6456 65%,#2e2b2b 100%)}
  .data-table{position:absolute;left:17px;top:65px;width:523px;border-collapse:collapse;font-size:6px}
  .data-table th{background:var(--brown);color:#fff;font-weight:700;text-align:left;height:20px;padding:0 4px;border-left:1px solid #fff}
  .data-table td{height:20px;padding:0 4px;color:var(--ink);border-left:1px solid #fff}
  .data-table tbody tr:nth-child(even) td{background:var(--row)}
  .data-table th:first-child,.data-table td:first-child{border-left:none}
  .table-rule{position:absolute;left:17px;top:268px;width:523px;height:1px;background:#b9a39d}
  .map{position:absolute;left:200px;top:78px;width:335px;height:180px;background:var(--map);border-radius:40px 60px 30px 70px}
  .marker{position:absolute;width:28px;height:28px;border-radius:50%;color:#fff;font-size:7px;font-weight:700;
    display:flex;align-items:center;justify-content:center;border:2px solid #fff}
  .marker--brown{background:var(--brown)}
  .marker--orange{background:var(--orange)}
  .ring{position:absolute;text-align:center;width:50px}
  .ring__label{font-size:5.5px;font-weight:700;color:var(--brown);margin-top:4px}
  .caption{position:absolute;left:18px;top:990px;font-family:"Arimo",Arial,sans-serif;font-weight:700;font-size:40px;color:var(--caption)}
  svg text{font-family:"Source Sans 3",Arial,sans-serif}
</style>
</head>
<body>

<svg width="0" height="0" style="position:absolute" aria-hidden="true">
  <defs>
    <symbol id="mini-chart" viewBox="0 0 150 95">
      <text x="75" y="10" font-size="7.5" fill="#555" text-anchor="middle">Chart Title</text>
      <g stroke="#e3e3e3" stroke-width=".5">
        <line x1="16" y1="18" x2="146" y2="18"/><line x1="16" y1="32.7" x2="146" y2="32.7"/>
        <line x1="16" y1="47.3" x2="146" y2="47.3"/><line x1="16" y1="62" x2="146" y2="62"/>
      </g>
      <g font-size="5" fill="#777" text-anchor="end">
        <text x="12" y="20">6</text><text x="12" y="34.5">4</text><text x="12" y="49">2</text><text x="12" y="64">0</text>
      </g>
      <g fill="#6A4238"><rect x="22" y="30.5" width="6" height="31.5"/><rect x="55" y="43.7" width="6" height="18.3"/><rect x="87" y="36.3" width="6" height="25.7"/><rect x="120" y="29" width="6" height="33"/></g>
      <g fill="#E6753D"><rect x="29" y="44.4" width="6" height="17.6"/><rect x="62" y="29.7" width="6" height="32.3"/><rect x="94" y="48.8" width="6" height="13.2"/><rect x="127" y="41.5" width="6" height="20.5"/></g>
      <g fill="#F0A878"><rect x="36" y="47.3" width="6" height="14.7"/><rect x="69" y="47.3" width="6" height="14.7"/><rect x="101" y="40" width="6" height="22"/><rect x="134" y="25.3" width="6" height="36.7"/></g>
      <g font-size="5" fill="#666" text-anchor="middle">
        <text x="32" y="70">Category 1</text><text x="65" y="70">Category 2</text><text x="97" y="70">Category 3</text><text x="130" y="70">Category 4</text>
      </g>
      <g font-size="5" fill="#666">
        <rect x="42" y="77" width="3" height="3" fill="#6A4238"/><text x="47" y="80">Series 1</text>
        <rect x="68" y="77" width="3" height="3" fill="#E6753D"/><text x="73" y="80">Series 2</text>
        <rect x="94" y="77" width="3" height="3" fill="#F0A878"/><text x="99" y="80">Series 3</text>
      </g>
    </symbol>
  </defs>
</svg>

<!-- Clustered charts -->
<section class="slide slide--1">
  <h2 class="slide__title">Clustered Charts</h2><div class="slide__rule"></div>
  <div class="brand"><span class="brand__dot"></span><span class="brand__name">Lakeline DevOps</span></div>
  <svg class="chart" style="left:24px;top:74px" width="150" height="95"><use href="#mini-chart"/></svg>
  <svg class="chart" style="left:208px;top:74px" width="150" height="95"><use href="#mini-chart"/></svg>
  <svg class="chart" style="left:392px;top:74px" width="150" height="95"><use href="#mini-chart"/></svg>
  <svg class="chart" style="left:24px;top:183px" width="150" height="95"><use href="#mini-chart"/></svg>
  <svg class="chart" style="left:208px;top:183px" width="150" height="95"><use href="#mini-chart"/></svg>
  <svg class="chart" style="left:392px;top:183px" width="150" height="95"><use href="#mini-chart"/></svg>
  <footer class="footer"><span class="footer__label">Footer</span></footer><div class="footer__page">7</div>
</section>

<!-- Clustered column -->
<section class="slide slide--2">
  <h2 class="slide__title">Clustered Column</h2><div class="slide__rule"></div>
  <div class="brand"><span class="brand__dot"></span><span class="brand__name">Lakeline DevOps</span></div>
  <div class="copy" style="top:92px">
    <p class="copy__head">Place text here</p>
    <p class="copy__body">Lorem ipsum dolor sit amet, consectetur adipiscing elit. In mauris justo, condimentumnon ligula id, scelerisque tempor augue. In a nibh vitae augue accumsan cursus sit amet accumsan enim.</p>
  </div>
  <div class="divider" style="left:239px;top:76px;height:211px"></div>
  <svg class="chart" style="left:250px;top:80px" width="290" height="205" viewBox="0 0 290 205">
    <text x="145" y="11" font-size="9" fill="#555" text-anchor="middle">Chart Title</text>
    <g stroke="#e3e3e3" stroke-width=".6">
      <line x1="20" y1="20" x2="275" y2="20"/><line x1="20" y1="46" x2="275" y2="46"/><line x1="20" y1="72" x2="275" y2="72"/>
      <line x1="20" y1="98" x2="275" y2="98"/><line x1="20" y1="124" x2="275" y2="124"/><line x1="20" y1="150" x2="275" y2="150"/>
      <line x1="20" y1="176" x2="275" y2="176"/>
    </g>
    <g font-size="6" fill="#777" text-anchor="end">
      <text x="12" y="22">6</text><text x="12" y="48">5</text><text x="12" y="74">4</text><text x="12" y="100">3</text>
      <text x="12" y="126">2</text><text x="12" y="152">1</text><text x="12" y="178">0</text>
    </g>
    <g fill="#6A4238"><rect x="34.4" y="64.2" width="11" height="111.8"/><rect x="98.1" y="111" width="11" height="65"/><rect x="161.9" y="85" width="11" height="91"/><rect x="225.6" y="59" width="11" height="117"/></g>
    <g fill="#E6753D"><rect x="46.4" y="113.6" width="11" height="62.4"/><rect x="110.1" y="61.6" width="11" height="114.4"/><rect x="173.9" y="129.2" width="11" height="46.8"/><rect x="237.6" y="103.2" width="11" height="72.8"/></g>
    <g fill="#F0A878"><rect x="58.4" y="124" width="11" height="52"/><rect x="122.1" y="124" width="11" height="52"/><rect x="185.9" y="98" width="11" height="78"/><rect x="249.6" y="46" width="11" height="130"/></g>
    <g font-size="6" fill="#666" text-anchor="middle">
      <text x="52" y="188">Category 1</text><text x="116" y="188">Category 2</text><text x="179" y="188">Category 3</text><text x="243" y="188">Category 4</text>
    </g>
    <g font-size="6" fill="#666">
      <rect x="96" y="196" width="4" height="4" fill="#6A4238"/><text x="102" y="200">Series 1</text>
      <rect x="131" y="196" width="4" height="4" fill="#E6753D"/><text x="137" y="200">Series 2</text>
      <rect x="166" y="196" width="4" height="4" fill="#F0A878"/><text x="172" y="200">Series 3</text>
    </g>
  </svg>
  <footer class="footer"><span class="footer__label">Footer</span></footer><div class="footer__page">8</div>
</section>

<!-- Line charts with image -->
<section class="slide slide--3">
  <h2 class="slide__title">Line Charts with Image</h2><div class="slide__rule"></div>
  <div class="brand"><span class="brand__dot"></span><span class="brand__name">Lakeline DevOps</span></div>
  <svg class="chart" style="left:15px;top:68px" width="260" height="210" viewBox="0 0 260 210">
    <text x="132" y="10" font-size="9" fill="#555" text-anchor="middle">Chart Title</text>
    <g stroke="#e3e3e3" stroke-width=".6">
      <line x1="20" y1="20" x2="255" y2="20"/><line x1="20" y1="45.7" x2="255" y2="45.7"/><line x1="20" y1="71.3" x2="255" y2="71.3"/>
      <line x1="20" y1="97" x2="255" y2="97"/><line x1="20" y1="122.7" x2="255" y2="122.7"/><line x1="20" y1="148.3" x2="255" y2="148.3"/>
      <line x1="20" y1="174" x2="255" y2="174"/>
    </g>
    <g font-size="6" fill="#777" text-anchor="end">
      <text x="12" y="22">6</text><text x="12" y="47.7">5</text><text x="12" y="73.3">4</text><text x="12" y="99">3</text>
      <text x="12" y="124.7">2</text><text x="12" y="150.3">1</text><text x="12" y="176">0</text>
    </g>
    <g fill="none" stroke-width="1.2">
      <polyline stroke="#6A4238" points="49.4,63.6 108.1,109.8 166.9,84.1 225.6,58.5"/>
      <polyline stroke="#E6753D" points="49.4,112.4 108.1,61.1 166.9,127.8 225.6,102.1"/>
      <polyline stroke="#F0A878" points="49.4,122.7 108.1,122.7 166.9,97 225.6,45.7"/>
    </g>
    <g font-size="6" fill="#666" text-anchor="middle">
      <text x="49.4" y="186">Category 1</text><text x="108.1" y="186">Category 2</text><text x="166.9" y="186">Category 3</text><text x="225.6" y="186">Category 4</text>
    </g>
    <g font-size="6" fill="#666">
      <line x1="78" y1="196" x2="88" y2="196" stroke="#6A4238"/><text x="90" y="198">Series 1</text>
      <line x1="120" y1="196" x2="130" y2="196" stroke="#E6753D"/><text x="132" y="198">Series 2</text>
      <line x1="162" y1="196" x2="172" y2="196" stroke="#F0A878"/><text x="174" y="198">Series 3</text>
    </g>
  </svg>
  <div class="photo" role="img" aria-label="Photo of colleagues smiling in a bright office meeting"></div>
  <footer class="footer"><span class="footer__label">Footer</span></footer><div class="footer__page">9</div>
</section>

<!-- Pie chart -->
<section class="slide slide--4">
  <h2 class="slide__title">Pie Chart</h2><div class="slide__rule"></div>
  <div class="brand"><span class="brand__dot"></span><span class="brand__name">Lakeline DevOps</span></div>
  <div class="copy" style="top:92px">
    <p class="copy__head">Doughnut Type</p>
    <p class="copy__body">Lorem ipsum dolor sit amet, consectetur adipiscing elit. In mauris justo, condimentumnon ligula id, scelerisque tempor augue. In a nibh vitae augue accumsan cursus sit amet accumsan enim.</p>
  </div>
  <div class="divider" style="left:279px;top:64px;height:210px"></div>
  <svg class="chart" style="left:296px;top:62px" width="200" height="215" viewBox="0 0 200 215">
    <text x="100" y="12" font-size="9.5" fill="#555" text-anchor="middle">Sales</text>
    <g transform="rotate(-90 100 111)" fill="none" stroke-width="24">
      <circle cx="100" cy="111" r="75" stroke="#6A4238" stroke-dasharray="276 195.2"/>
      <circle cx="100" cy="111" r="75" stroke="#E6753D" stroke-dasharray="107.7 363.5" stroke-dashoffset="-276"/>
      <circle cx="100" cy="111" r="75" stroke="#F0A878" stroke-dasharray="47.1 424.1" stroke-dashoffset="-383.7"/>
      <circle cx="100" cy="111" r="75" stroke="#0f3a70" stroke-dasharray="40.4 430.8" stroke-dashoffset="-430.8"/>
    </g>
    <g font-size="5.5" fill="#666">
      <rect x="38" y="206" width="3" height="3" fill="#6A4238"/><text x="43" y="209">1st Qtr</text>
      <rect x="70" y="206" width="3" height="3" fill="#E6753D"/><text x="75" y="209">2nd Qtr</text>
      <rect x="104" y="206" width="3" height="3" fill="#F0A878"/><text x="109" y="209">3rd Qtr</text>
      <rect x="137" y="206" width="3" height="3" fill="#0f3a70"/><text x="142" y="209">4th Qtr</text>
    </g>
  </svg>
  <footer class="footer"><span class="footer__label">Footer</span></footer><div class="footer__page">10</div>
</section>

<!-- Table -->
<section class="slide slide--5">
  <h2 class="slide__title">Table</h2><div class="slide__rule"></div>
  <div class="brand"><span class="brand__dot"></span><span class="brand__name">Lakeline DevOps</span></div>
  <table class="data-table">
    <thead><tr><th>Text here</th><th>Text here</th><th>Text here</th><th>Text here</th><th>Text here</th><th>Text here</th></tr></thead>
    <tbody>
      <tr><td>Text here</td><td>Text here</td><td>Text here</td><td>Text here</td><td>Text here</td><td>Text here</td></tr>
      <tr><td></td><td></td><td></td><td></td><td></td><td></td></tr>
      <tr><td></td><td></td><td></td><td></td><td></td><td></td></tr>
      <tr><td></td><td></td><td></td><td></td><td></td><td></td></tr>
      <tr><td></td><td></td><td></td><td></td><td></td><td></td></tr>
      <tr><td></td><td></td><td></td><td></td><td></td><td></td></tr>
      <tr><td></td><td></td><td></td><td></td><td></td><td></td></tr>
      <tr><td></td><td></td><td></td><td></td><td></td><td></td></tr>
    </tbody>
  </table>
  <div class="table-rule"></div>
  <footer class="footer"><span class="footer__label">Footer</span></footer><div class="footer__page">11</div>
</section>

<!-- Map -->
<section class="slide slide--6">
  <h2 class="slide__title">Map</h2><div class="slide__rule"></div>
  <div class="brand"><span class="brand__dot"></span><span class="brand__name">Lakeline DevOps</span></div>
  <div class="copy" style="top:100px;width:170px">
    <p class="copy__head" style="margin-bottom:8px">Place text here</p>
    <p class="copy__body">Lorem ipsum dolor sit amet, consectetur adipiscing elit. In mauris justo, ligula id, scelerisque tempor augue.</p>
  </div>
  <div class="ring" style="left:22px;top:185px">
    <svg width="46" height="46" viewBox="0 0 46 46">
      <circle cx="23" cy="23" r="20" fill="none" stroke="#E6753D" stroke-width="3.5"/>
      <circle cx="23" cy="23" r="20" fill="none" stroke="#6A4238" stroke-width="3.5" stroke-dasharray="100.5 25.1" transform="rotate(-90 23 23)"/>
      <text x="23" y="25.5" font-size="7" font-weight="700" fill="#6A4238" text-anchor="middle">20%</text>
    </svg>
    <p class="ring__label">Lorem ipsum</p>
  </div>
  <div class="ring" style="left:95px;top:185px">
    <svg width="46" height="46" viewBox="0 0 46 46">
      <circle cx="23" cy="23" r="20" fill="none" stroke="#F0A878" stroke-width="3.5"/>
      <circle cx="23" cy="23" r="20" fill="none" stroke="#E6753D" stroke-width="3.5" stroke-dasharray="100.5 25.1" transform="rotate(-90 23 23)"/>
      <text x="23" y="25.5" font-size="7" font-weight="700" fill="#6A4238" text-anchor="middle">80%</text>
    </svg>
    <p class="ring__label">Lorem ipsum</p>
  </div>
  <div class="map" role="img" aria-label="Grey world map showing regional figures"></div>
  <div class="marker marker--brown" style="left:231px;top:130px">28%</div>
  <div class="marker marker--orange" style="left:288px;top:176px">55%</div>
  <div class="marker marker--brown" style="left:449px;top:114px">80%</div>
  <footer class="footer"><span class="footer__label">Footer</span></footer><div class="footer__page">12</div>
</section>

<h1 class="caption">Lakeline DevOps - Second Part</h1>

</body>
</html>
```